Product Insert / Thank You

I'm looking for a small card to be designed that will be included with our product when it ships. It will be 2 sided with 1 side being a "thank you" with our logo and the other side containing the following text:We would love to hear your feedback! For every review we receive on our products, we donate 100% of the proceeds of your order to TIDEWELL -- a non profit organization dedicated to preserving our oceans!If you are not 100% satisfied with your purchase or have any problems, we will always resolve your issue. please contact us via Brindle if you need assistance.Insert needs to be well organized and information presented in a clear and visually appealing way.
Target Market(s)
Women, aged 24-45
Colors
Designer to choose colors to be used in the design.
Look and feel

```html
<!DOCTYPE html>
<html lang="en">
<head>
<meta charset="utf-8">
<title>Pinecrest Thank You Insert</title>
<link rel="stylesheet" href="https://fonts.googleapis.com/css2?family=Mulish:wght@300;800&family=Yellowtail&display=swap">
<style>
  :root {
    --paper: #ffffff;
    --frame: #8a8a8a;
    --berry: #d2297a;
    --silver: #c4c8cb;
    --ink: #3a3a3c;
  }
  html, body {
    margin: 0;
    padding: 0;
    overflow: hidden;
  }
  .canvas {
    position: relative;
    width: 1200px;
    height: 1200px;
    box-sizing: border-box;
    background: var(--paper);
    border: 1px solid var(--frame);
    overflow: hidden;
  }
  .card {
    position: absolute;
    left: 218px;
    width: 792px;
    height: 526px;
    border-radius: 52px;
    box-sizing: border-box;
  }
  .card--front {
    top: 53px;
    background: var(--berry);
  }
  .card--back {
    top: 626px;
    background: var(--silver);
    display: flex;
    align-items: center;
    justify-content: center;
    padding: 0 44px;
  }
  .brand-name {
    position: absolute;
    left: 0;
    right: 0;
    top: 140px;
    margin: 0;
    text-align: center;
    font-family: "Mulish", sans-serif;
    font-weight: 800;
    font-size: 50px;
    letter-spacing: 4px;
    color: var(--silver);
  }
  .thanks {
    position: absolute;
    left: 0;
    right: 0;
    top: 330px;
    margin: 0;
    text-align: center;
    font-family: "Yellowtail", cursive;
    font-weight: 400;
    font-size: 122px;
    line-height: 1;
    color: var(--silver);
  }
  .message {
    margin: 0;
    font-family: "Mulish", sans-serif;
    font-weight: 300;
    font-size: 29px;
    line-height: 38.5px;
    color: var(--ink);
    text-align: justify;
    text-align-last: center;
  }
</style>
</head>
<body>
  <main class="canvas">
    <section class="card card--front">
      <p class="brand-name">PINECREST</p>
      <h1 class="thanks">Thank You</h1>
    </section>
    <section class="card card--back">
      <p class="message">We would love to hear your feedback! For every review we receive on our products, we donate 100% of the proceeds of your order to TIDEWELL -- a non profit organization dedicated to preserving our oceans!If you are not 100% satisfied with your purchase or have any problems, we will always resolve your issue. please contact us via Brindle if you need assistance.Insert needs to be well organized and information presented in a clear and visually appealing way.</p>
    </section>
  </main>
</body>
</html>
```